Business Card Design - Property Management & Real Estate Services

I need a business card design for my company that I can print Pell Prints. The company is called Tarrow Management Company. It is a property management and real estate company. The design has to be clean and modern. I need two versions. One for my employee and one for me. However, the design will be the same, just different text. You can get a feel for the company by looking at our website at www.tarrowmanagement.example.

Industry/Entity Type

Property Management

Contact Information for Business Card

I will be using Pell.com to print my cards. I will most likely use the rounded edges card. I need two versions, however, they will be the same design. I need one for me and my employee.

Colors
3276b5
33a6d7

Requirements
Must have
• Company Logo
• Name of person
• Property Management & Real Estate Service
• Phone
• Email
• Website
• Address
• A space to place a QR code

```html
<!DOCTYPE html>
<html lang="en">
<head>
<meta charset="utf-8">
<title>Tarrow Management – Business Card</title>
<link href="https://fonts.googleapis.com/css2?family=Roboto:wght@400;500&family=Roboto+Condensed:wght@700&display=swap" rel="stylesheet">
<style>
  :root {
    --backdrop: #d4d4d6;
    --card-front: #6699cc;
    --brand-deep: #1f4e9c;
    --brand-mid: #3276b5;
    --brand-light: #6f9fd4;
    --paper: #f7f7f8;
    --ink: #3a3a3a;
  }
  * { box-sizing: border-box; margin: 0; padding: 0; }
  html, body { width: 1200px; height: 852px; overflow: hidden; }
  body {
    background: var(--backdrop);
    font-family: "Roboto", Arial, sans-serif;
    position: relative;
  }
  .card {
    position: absolute;
    top: 278px;
    width: 520px;
    height: 297px;
    border-radius: 16px;
    overflow: hidden;
    box-shadow: 0 6px 16px rgba(0,0,0,0.18);
  }
  .card--front { left: 60px; background: var(--card-front); }
  .card--back { left: 620px; background: var(--paper); }

  .wordmark {
    display: flex;
    align-items: center;
    gap: 12px;
    color: var(--brand-deep);
    font-family: "Roboto", Arial, sans-serif;
    font-weight: 500;
    line-height: 1;
  }
  .wordmark__square { width: 18px; height: 18px; background: var(--brand-deep); flex: none; }
  .card--front .wordmark {
    position: absolute; left: 0; right: 0; top: 50%;
    transform: translateY(-50%);
    justify-content: center;
    font-size: 42px;
    letter-spacing: 2px;
  }
  .card--back .wordmark {
    position: absolute; left: 36px; top: 58px;
    font-size: 34px; letter-spacing: 1px;
  }
  .card--back .wordmark__square { width: 16px; height: 16px; }

  .person { position: absolute; left: 36px; top: 150px; }
  .person__name {
    font-family: "Roboto Condensed", "Arial Narrow", sans-serif;
    font-weight: 700; font-size: 20px; color: var(--brand-deep);
  }
  .person__role { font-size: 13px; color: var(--ink); margin-top: 4px; }
  .person__address { font-size: 13px; color: var(--ink); line-height: 1.45; margin-top: 24px; }

  .contact {
    position: absolute; left: 272px; top: 112px;
    list-style: none; font-size: 12.5px; color: var(--ink);
  }
  .contact li { display: flex; align-items: center; gap: 8px; margin-bottom: 6px; }
  .contact svg { width: 12px; height: 12px; fill: var(--brand-deep); flex: none; }

  .base-strip {
    position: absolute; left: 0; right: 0; bottom: 0; height: 12px;
    background: var(--brand-light);
  }
  .tagline-band {
    position: absolute; right: 0; bottom: 0;
    width: 276px; height: 44px;
    background: var(--brand-deep);
    border-top-left-radius: 14px;
    color: #fff; font-size: 11.5px; font-weight: 500;
    display: flex; align-items: center; justify-content: center;
  }
</style>
</head>
<body>

  <section class="card card--front" aria-label="Card front">
    <div class="wordmark">
      <span class="wordmark__square"></span>
      <span>Tarrow Management</span>
    </div>
  </section>

  <section class="card card--back" aria-label="Card back">
    <div class="wordmark">
      <span class="wordmark__square"></span>
      <span>Tarrow Management</span>
    </div>

    <div class="person">
      <p class="person__name">Marcos T. Ellery</p>
      <p class="person__role">Founder</p>
      <p class="person__address">480 Harbor Ave<br>#210 Miami, FL 33130</p>
    </div>

    <ul class="contact">
      <li>
        <svg viewBox="0 0 24 24" aria-hidden="true"><path d="M6.6 10.8a15.1 15.1 0 0 0 6.6 6.6l2.2-2.2a1 1 0 0 1 1-.25 11.4 11.4 0 0 0 3.6.57 1 1 0 0 1 1 1V20a1 1 0 0 1-1 1A17 17 0 0 1 3 4a1 1 0 0 1 1-1h3.5a1 1 0 0 1 1 1c0 1.25.2 2.45.57 3.57a1 1 0 0 1-.25 1z"/></svg>
        (305) 555-0142
      </li>
      <li>
        <svg viewBox="0 0 24 24" aria-hidden="true"><path d="M2 5h20v14H2z M2 5l10 8 10-8" fill="none" stroke="currentColor"/><path d="M2 5h20v2l-10 7L2 7z"/><path d="M2 8l10 7 10-7v11H2z"/></svg>
        marcos@tarrowmanagement.example
      </li>
      <li>
        <svg viewBox="0 0 24 24" aria-hidden="true"><circle cx="12" cy="12" r="10"/><path d="M2 12h20M12 2c3 3 3 17 0 20M12 2c-3 3-3 17 0 20" stroke="#f7f7f8" stroke-width="1.5" fill="none"/></svg>
        www.tarrowmanagement.example
      </li>
    </ul>

    <div class="base-strip"></div>
    <div class="tagline-band">Miami Property Management &amp; Real Estate Services</div>
  </section>

</body>
</html>
```